Business card and stationary design for a digital advertising agency

We look to get designs for
- Business card
- Envelope C5 & A4
- Letterhead A4
- Thin Folder (to place the brochures and quotes in. There must be places to put the cd envelope and a business card inside the file as well as a place for the papers)
- CD label & envelope
- Notepad
- Mousepad

We are open for all kind of creativity but please have a look at our website to have an idea. (The website is not ready at the moment but you can see the colours, get the logo, etc.)

Link: www.trelvanix.com/anasayfa

PLEASE NOTE: In the logo file, there are 2 logos but we only use the one on top. We never use the one at the bottom!
Updates

Please use the attached ForDesign.zip file to use the background pattern of our website, inside the folder img there are background patterns of our website. Please use the background or at least inspire from that files in order to design our brochures.  

All designers, please bear in mind that firstly we need the samples of each items described in the brief. Then we will comment on each of them. 

Please submit the designs for all the items at once.

Thanks!

TrelVanix

Target Market(s)

Our customers are the companies who will advertise on internet and digital media and we work mainly in Turkish market

Industry/Entity Type

Digital

Requirements
Must have
• Please use the attached ForDesign.zip file to use the background pattern of our website, inside the folder img there are background patterns of our website. Please use the background or at least inspire from that files in order to design our brochures.
Should not have
• Too much colours such as a child's colouring book.

```html
<!DOCTYPE html>
<html lang="en">
<head>
<meta charset="utf-8">
<title>TrelVanix – CD Label and Sleeve</title>
<link rel="stylesheet" href="https://fonts.googleapis.com/css2?family=Questrial&family=Didact+Gothic&display=swap">
<style>
  :root {
    --stage: #8e8e8e;
    --paper: #ffffff;
    --ink: #111111;
    --brand-grey: #5a5a5a;
    --accent: #e8453c;
    --pattern-dark: #0d0d0d;
    --pattern-magenta: #d63a8f;
    --pattern-yellow: #e9d33a;
    --pattern-green: #7cc24a;
    --pattern-blue: #5aa9d8;
  }
  html, body {
    margin: 0;
    padding: 0;
    width: 1200px;
    height: 848px;
    overflow: hidden;
    background: var(--stage);
  }
  .canvas {
    position: relative;
    width: 1200px;
    height: 848px;
    font-family: "Didact Gothic", "Questrial", sans-serif;
  }

  /* Sleeve */
  .sleeve-flap {
    position: absolute;
    left: 137px;
    top: 178px;
    width: 378px;
    height: 52px;
  }
  .sleeve {
    position: absolute;
    left: 137px;
    top: 230px;
    width: 378px;
    height: 378px;
    background: var(--paper);
  }
  .sleeve .identity {
    position: absolute;
    left: 132px;
    top: 138px;
  }

  /* Disc */
  .disc {
    position: absolute;
    left: 595px;
    top: 232px;
    width: 376px;
    height: 376px;
    border-radius: 50%;
    background: var(--paper);
    overflow: hidden;
  }
  .disc-band {
    position: absolute;
    left: 0;
    top: 0;
    width: 376px;
    height: 376px;
  }
  .disc .identity {
    position: absolute;
    left: 242px;
    top: 140px;
  }

  /* Shared identity block */
  .wordmark {
    display: flex;
    align-items: center;
    gap: 4px;
    font-family: "Questrial", sans-serif;
    font-size: 25px;
    line-height: 1;
    color: var(--brand-grey);
    letter-spacing: -0.3px;
    margin: 0;
  }
  .wordmark-dot {
    width: 6px;
    height: 6px;
    background: var(--accent);
    align-self: flex-start;
  }
  .contact {
    list-style: none;
    margin: 18px 0 0;
    padding: 0;
    font-size: 7.2px;
    line-height: 9.4px;
    color: var(--ink);
    font-weight: 700;
  }
  .contact .key {
    color: #777;
    font-weight: 400;
    margin-right: 2px;
  }
  .disc .contact { margin-top: 16px; }
</style>
</head>
<body>
<main class="canvas">

  <svg class="sleeve-flap" viewBox="0 0 378 52" role="img" aria-label="Colourful scattered-squares pattern on a dark flap">
    <defs>
      <linearGradient id="flap-pattern" x1="0" y1="0" x2="1" y2="0">
        <stop offset="0" stop-color="#1a1a1a"/>
        <stop offset="0.18" stop-color="var(--pattern-green)"/>
        <stop offset="0.35" stop-color="var(--pattern-magenta)"/>
        <stop offset="0.55" stop-color="#9fc46a"/>
        <stop offset="0.75" stop-color="var(--pattern-yellow)"/>
        <stop offset="0.9" stop-color="var(--pattern-magenta)"/>
        <stop offset="1" stop-color="#1a1a1a"/>
      </linearGradient>
      <linearGradient id="flap-fade" x1="0" y1="0" x2="0" y2="1">
        <stop offset="0" stop-color="#000" stop-opacity="0.55"/>
        <stop offset="0.6" stop-color="#000" stop-opacity="0"/>
        <stop offset="1" stop-color="#fff" stop-opacity="0.35"/>
      </linearGradient>
    </defs>
    <polygon points="15,0 363,0 378,52 0,52" fill="url(#flap-pattern)"/>
    <polygon points="15,0 363,0 378,52 0,52" fill="url(#flap-fade)"/>
  </svg>

  <section class="sleeve" aria-label="CD sleeve">
    <div class="identity">
      <p class="wordmark">TrelVanix<span class="wordmark-dot"></span></p>
      <ul class="contact">
        <li><span class="key">C:</span> 0700 555 014 / 0700 555 027</li>
        <li><span class="key">W:</span> www.trelvanix.com/anasayfa</li>
        <li><span class="key">E:</span> mkaya@trelvanix.com</li>
        <li><span class="key">M:</span> P.o Box 100482 Earth.</li>
      </ul>
    </div>
  </section>

  <section class="disc" aria-label="CD label">
    <svg class="disc-band" viewBox="0 0 376 376">
      <defs>
        <linearGradient id="band-pattern" x1="0" y1="0" x2="1" y2="0">
          <stop offset="0" stop-color="var(--pattern-blue)"/>
          <stop offset="0.25" stop-color="var(--pattern-green)"/>
          <stop offset="0.45" stop-color="#e86a4a"/>
          <stop offset="0.62" stop-color="var(--pattern-yellow)"/>
          <stop offset="0.78" stop-color="var(--pattern-dark)"/>
          <stop offset="1" stop-color="var(--pattern-dark)"/>
        </linearGradient>
      </defs>
      <path d="M0 145 H192 A43 43 0 0 1 192 231 H0 Z" fill="url(#band-pattern)" role="img" aria-label="Colourful scattered-squares pattern fading into black"/>
      <circle class="disc-hub" cx="188" cy="188" r="37" fill="var(--paper)"/>
    </svg>
    <div class="identity">
      <p class="wordmark">TrelVanix<span class="wordmark-dot"></span></p>
      <ul class="contact">
        <li><span class="key">C:</span> 0700 555 014 / 0700 555 027</li>
        <li><span class="key">W:</span> www.trelvanix.com/anasayfa</li>
        <li><span class="key">E:</span> mkaya@trelvanix.com</li>
        <li><span class="key">M:</span> P.o Box 100482 Earth.</li>
      </ul>
    </div>
  </section>

</main>
</body>
</html>
```